Silver Brook Decorators Banner

Create a banner that displays and reinforces Silver Brook Decorators’ brand identity while promoting our interior painting services. The banner will be displayed at indoor venues through the winter. The design should be clean, professional, and visually recognizable to both new and returning customers. See attached design brief & logo source files.

```html
<!DOCTYPE html>
<html lang="en">
<head>
<meta charset="utf-8">
<title>Silver Brook Decorators Banner</title>
<link rel="stylesheet" href="https://fonts.googleapis.com/css2?family=Bebas+Neue&family=Poppins:wght@600;700;800&display=swap">
<style>
  :root {
    --page-bg: #7f8a7e;
    --banner-dark: #1f201f;
    --banner-mid: #2c2d2c;
    --brand-green: #7dbd5c;
    --brand-green-deep: #5e9a45;
    --ink: #1c1d1c;
    --white: #ffffff;
    --divider: rgba(255,255,255,0.55);
  }
  * { margin: 0; padding: 0; box-sizing: border-box; }
  html, body { width: 1054px; height: 1200px; overflow: hidden; }
  body { background: var(--page-bg); position: relative; font-family: "Poppins", sans-serif; }

  .banner {
    position: absolute; left: 47px; top: 408px; width: 960px; height: 383px;
    background: var(--banner-dark); overflow: hidden;
    box-shadow: 0 10px 30px rgba(0,0,0,0.35);
  }
  .banner__backdrop {
    position: absolute; inset: 0;
    background: linear-gradient(100deg, #232423 0%, #2e2f2e 45%, #262726 70%, #1d1e1d 100%);
  }
  .headline {
    position: absolute; left: 36px; top: 22px;
    font-family: "Bebas Neue", sans-serif; font-size: 137px; line-height: 1;
    color: var(--white); letter-spacing: 0.5px; white-space: nowrap;
  }
  .tagline {
    position: absolute; left: 40px; top: 145px; width: 636px; height: 40px;
    background: var(--brand-green); border-radius: 9px;
    display: flex; align-items: center; justify-content: center;
    font-weight: 700; font-size: 24px; letter-spacing: 5.4px; color: var(--ink);
  }
  .brand-name {
    position: absolute; left: 708px; top: 62px; width: 212px;
    font-weight: 800; font-size: 31px; line-height: 1.12; color: var(--white);
    text-align: center; letter-spacing: 0.5px;
  }
  .brand-mark {
    position: absolute; left: 796px; top: 24px; width: 34px; height: 34px;
    border-radius: 50%; background: var(--brand-green);
  }
  .services { position: absolute; left: 0; top: 198px; width: 960px; height: 88px; }
  .service {
    position: absolute; top: 0; width: 200px; margin-left: -100px; text-align: center;
  }
  .service__icon { display: block; margin: 0 auto; height: 44px; }
  .service__label {
    display: block; margin-top: 6px; font-weight: 700; font-size: 25px; line-height: 1.2; color: var(--white);
  }
  .service-divider {
    position: absolute; top: 3px; height: 80px; border-left: 1.5px dashed var(--divider);
  }
  .cta {
    position: absolute; left: 37px; top: 303px; width: 878px; height: 54px;
    border-radius: 27px; background: var(--brand-green); overflow: hidden;
  }
  .cta__lead {
    position: absolute; left: 22px; top: 0; line-height: 54px;
    font-weight: 700; font-size: 26px; color: var(--ink); letter-spacing: -0.3px;
  }
  .cta__link {
    position: absolute; left: 400px; top: 0; right: 0; height: 54px;
    background: var(--white); border-radius: 27px;
    display: flex; align-items: center; gap: 14px; padding-left: 16px;
  }
  .cta__url { font-weight: 800; font-size: 32px; color: var(--ink); letter-spacing: -0.4px; }
  .cta__url-domain { color: var(--brand-green-deep); }
</style>
</head>
<body>
  <section class="banner">
    <div class="banner__backdrop" role="img" aria-label="Faint photo of a bright painted interior room behind the banner content"></div>

    <h1 class="headline">PAINT SMARTER</h1>
    <div class="tagline">INTERIOR PAINTING SERVICES</div>

    <span class="brand-mark"></span>
    <div class="brand-name">SILVER BROOK<br>DECORATORS</div>

    <div class="services">
      <div class="service" style="left:88px">
        <svg class="service__icon" viewBox="0 0 44 44" width="44" aria-hidden="true">
          <path d="M4 2h30v8H13v32H4z" fill="var(--brand-green)"/>
          <rect x="18" y="11" width="22" height="7" rx="1" fill="var(--white)"/>
          <path d="M16 14h2v8h10v5" stroke="var(--white)" stroke-width="2" fill="none"/>
          <rect x="26" y="27" width="4" height="13" fill="var(--white)"/>
        </svg>
        <span class="service__label">Walls</span>
      </div>
      <span class="service-divider" style="left:161px"></span>

      <div class="service" style="left:248px">
        <svg class="service__icon" viewBox="0 0 48 44" width="48" aria-hidden="true">
          <rect x="2" y="2" width="44" height="6" fill="var(--white)"/>
          <rect x="22.5" y="8" width="3" height="14" fill="var(--brand-green)"/>
          <path d="M10 36 Q24 18 38 36z" fill="var(--brand-green)"/>
          <circle cx="24" cy="39" r="3" fill="var(--brand-green)"/>
        </svg>
        <span class="service__label">Ceilings</span>
      </div>
      <span class="service-divider" style="left:337px"></span>

      <div class="service" style="left:403px">
        <svg class="service__icon" viewBox="0 0 30 44" width="30" aria-hidden="true">
          <rect x="6" y="2" width="18" height="38" fill="var(--brand-green)"/>
          <rect x="8" y="4" width="14" height="34" fill="none" stroke="var(--brand-green-deep)" stroke-width="1"/>
          <circle cx="19" cy="22" r="1.3" fill="var(--white)"/>
          <rect x="2" y="40" width="26" height="3" fill="var(--white)"/>
        </svg>
        <span class="service__label">Trim</span>
      </div>
      <span class="service-divider" style="left:468px"></span>

      <div class="service" style="left:567px">
        <svg class="service__icon" viewBox="0 0 44 44" width="44" aria-hidden="true">
          <rect x="3" y="3" width="17" height="10" fill="var(--brand-green)"/>
          <rect x="23" y="3" width="18" height="20" fill="var(--brand-green)"/>
          <rect x="3" y="16" width="17" height="7" fill="var(--brand-green)"/>
          <rect x="3" y="26" width="17" height="15" fill="var(--white)"/>
          <rect x="23" y="26" width="18" height="15" fill="var(--brand-green)"/>
          <rect x="8" y="31" width="2" height="5" fill="var(--ink)"/>
          <rect x="12" y="31" width="2" height="5" fill="var(--ink)"/>
        </svg>
        <span class="service__label">Cabinets</span>
      </div>
      <span class="service-divider" style="left:663px"></span>

      <div class="service" style="left:801px">
        <svg class="service__icon" viewBox="0 0 40 44" width="40" aria-hidden="true">
          <rect x="20" y="2" width="16" height="40" fill="var(--brand-green)"/>
          <path d="M10 12 L30 28 L14 34z" fill="var(--white)"/>
          <rect x="3" y="32" width="12" height="5" rx="2" transform="rotate(-40 9 34)" fill="var(--brand-green)"/>
        </svg>
        <span class="service__label">Drywall Repair</span>
      </div>
    </div>

    <div class="cta">
      <span class="cta__lead">Book a Free Estimate at</span>
      <div class="cta__link">
        <svg viewBox="0 0 26 26" width="26" height="26" aria-hidden="true">
          <circle cx="13" cy="13" r="11" fill="none" stroke="var(--brand-green)" stroke-width="2"/>
          <ellipse cx="13" cy="13" rx="5" ry="11" fill="none" stroke="var(--brand-green)" stroke-width="2"/>
          <path d="M2 13h22M4 7h18M4 19h18" stroke="var(--brand-green)" stroke-width="2"/>
        </svg>
        <span class="cta__url">www.<span class="cta__url-domain">sbdecorators</span>.com</span>
      </div>
    </div>
  </section>
</body>
</html>
```